Business Cards for a small business advisory (business services)

Professional look. Same as would apply for a lawyer, accountant, or other financial services professional. Please use the logo colors

Target Market(s)

small business owners

Industry/Entity Type

Financial Servics

Contact Information for Business Card

Name: Gavin L. Whitmore, CAIA / Title: Business Advisor / Office #: (718) 294-7716 / Mobile #: (917) 382-5047 / Email: g.whitmore@clearfieldventurepartners.example / Web: www.clearfieldventurepartners.example

Font styles to use
Sans Serif

```html
<!DOCTYPE html>
<html lang="en">
<head>
<meta charset="utf-8">
<title>Clearfield Venture Partners – Business Cards</title>
<link href="https://fonts.googleapis.com/css2?family=Source+Sans+3:ital,wght@0,400;0,600;0,700;1,400&display=swap" rel="stylesheet">
<style>
  :root {
    --navy: #1d3a6b;
    --green: #8cc63f;
    --stage: #a2a2a2;
    --card: #ffffff;
    --pattern: #f6f6f6;
  }
  * { margin: 0; padding: 0; box-sizing: border-box; }
  html, body { width: 1200px; height: 1130px; overflow: hidden; background: var(--stage); }
  body { position: relative; font-family: "Source Sans 3", sans-serif; color: var(--navy); }

  .card { position: absolute; left: 185px; width: 829px; height: 474px; background: var(--card); overflow: hidden; }
  .card--front { top: 61px; }
  .card--back { top: 591px; }

  .pattern-fill { position: absolute; inset: 0; background: var(--pattern); }

  .brand { position: absolute; display: flex; align-items: center; gap: 14px; font-family: "Source Sans 3", sans-serif; font-weight: 600; color: var(--navy); white-space: nowrap; }
  .brand__dot { border-radius: 50%; background: var(--navy); flex: none; }
  .card--front .brand { left: 0; right: 0; top: 262px; justify-content: center; font-size: 46px; }
  .card--front .brand__dot { width: 40px; height: 40px; }
  .card--back .brand { right: 35px; top: 40px; font-size: 28px; gap: 10px; }
  .card--back .brand__dot { width: 24px; height: 24px; }

  .front-web { position: absolute; left: 0; right: 0; top: 402px; display: flex; align-items: center; justify-content: center; gap: 18px; }
  .front-web__rule { width: 214px; height: 2px; background: linear-gradient(90deg, transparent, var(--green) 25%, var(--green) 75%, transparent); }
  .front-web__url { font-style: italic; font-size: 19px; color: var(--navy); }

  .person { position: absolute; left: 35px; top: 207px; }
  .person__name { font-weight: 700; font-size: 31px; letter-spacing: 0.2px; line-height: 1; text-transform: uppercase; }
  .person__title { font-size: 19px; margin-top: 14px; }
  .person__rule { width: 217px; height: 2px; margin-top: 14px; background: linear-gradient(90deg, transparent, var(--green) 15%, var(--green) 85%, transparent); }

  .contacts { position: absolute; left: 35px; top: 306px; list-style: none; }
  .contacts li { display: flex; align-items: center; gap: 10px; font-size: 19px; height: 24px; }
  .contacts li + li { margin-top: 11px; }
  .contacts svg { width: 22px; height: 22px; flex: none; fill: none; stroke: var(--green); stroke-width: 1.4; stroke-linecap: round; stroke-linejoin: round; }
</style>
</head>
<body>

<section class="card card--front">
  <div class="pattern-fill" role="img" aria-label="Faint repeating star pattern background"></div>
  <div class="brand"><span class="brand__dot"></span>Clearfield Venture Partners</div>
  <div class="front-web">
    <span class="front-web__rule"></span>
    <span class="front-web__url">www.clearfieldventurepartners.example</span>
    <span class="front-web__rule"></span>
  </div>
</section>

<section class="card card--back">
  <div class="brand"><span class="brand__dot"></span>Clearfield Venture Partners</div>

  <div class="person">
    <h1 class="person__name">Gavin L. Whitmore, CAIA</h1>
    <p class="person__title">Business Advisor</p>
    <div class="person__rule"></div>
  </div>

  <ul class="contacts">
    <li>
      <svg viewBox="0 0 22 22"><rect x="6" y="2" width="10" height="18" rx="1.5"/><line x1="9.5" y1="17" x2="12.5" y2="17"/></svg>
      (718) 294-7716
    </li>
    <li>
      <svg viewBox="0 0 22 22"><path d="M5 3l3 0 1.5 4-2 1.5c1 2.5 3 4.5 5.5 5.5l1.5-2 4 1.5v3c0 1-1 2-2 2C9.5 18.5 3.5 12.5 3 5c0-1 1-2 2-2z"/><path d="M13 3a6 6 0 0 1 6 6"/><path d="M13 6a3 3 0 0 1 3 3"/></svg>
      (917) 382-5047
    </li>
    <li>
      <svg viewBox="0 0 22 22"><path d="M2 9l9-6 9 6v11H2z"/><path d="M2 9l9 6 9-6"/><path d="M2 20l7-6M20 20l-7-6"/></svg>
      g.whitmore@clearfieldventurepartners.example
    </li>
    <li>
      <svg viewBox="0 0 22 22"><circle cx="11" cy="11" r="9"/><ellipse cx="11" cy="11" rx="4" ry="9"/><line x1="2" y1="11" x2="20" y2="11"/><path d="M3.5 6.5h15M3.5 15.5h15"/></svg>
      www.clearfieldventurepartners.example
    </li>
  </ul>
</section>

</body>
</html>
```